Kinesiology undergraduate program needs an infographic

We would like an infographic to creatively and succinctly inform students, faculty, staff, and others about our undergraduate values and competencies (perhaps also integrating our mission and vision). We would like to see a design that incorporates the definition of Kinesiology (the study of human movement) and the colors of our Westbrook State University at Larkfield.

```html
<!DOCTYPE html>
<html lang="en">
<head>
<meta charset="utf-8">
<title>Kinesiology Undergraduate Program – Mission, Values and Vision</title>
<link rel="stylesheet" href="https://fonts.googleapis.com/css2?family=Archivo+Black&family=Montserrat:wght@400;800&display=swap">
<style>
  :root {
    --brand-red: #d50f25;
    --ink-navy: #1f2147;
    --text-dark: #1c1c1c;
    --halo-grey: #ececec;
    --paper: #ffffff;
  }
  * { margin: 0; padding: 0; box-sizing: border-box; }
  html, body { width: 1200px; height: 848px; overflow: hidden; background: var(--paper); }
  .infographic {
    position: relative; width: 1200px; height: 848px; overflow: hidden;
    font-family: "Montserrat", sans-serif; color: var(--text-dark);
  }
  .graphics { position: absolute; inset: 0; }

  .college-name {
    position: absolute; left: 42px; top: 44px; width: 130px;
    font-family: "Montserrat", sans-serif; font-weight: 800; font-size: 12px;
    line-height: 15px; color: var(--brand-red);
  }

  .statement { position: absolute; text-align: center; }
  .statement__title {
    font-family: "Archivo Black", sans-serif; color: var(--brand-red);
    font-size: 47px; line-height: 54px; text-transform: uppercase;
  }
  .statement__body { font-size: 16px; line-height: 20.6px; }
  .statement--mission { left: 435px; top: 28px; width: 330px; }
  .statement--values { left: 116px; top: 140px; width: 240px; }
  .statement--vision { left: 817px; top: 156px; width: 290px; }
  .statement__arrow {
    width: 0; height: 0; margin: 14px auto 0; transform: translateX(-10px);
    border-left: 9px solid transparent; border-right: 9px solid transparent;
    border-top: 16px solid var(--ink-navy);
  }

  .competency { position: absolute; }
  .competency__title {
    font-family: "Archivo Black", sans-serif; color: var(--ink-navy);
    font-size: 16px; line-height: 20px; text-transform: uppercase;
  }
  .competency__list { list-style: none; margin-top: 1px; }
  .competency__list li { font-size: 17px; line-height: 20.6px; position: relative; }
  .competency__list li::before {
    content: "•"; position: absolute; left: -15px; color: var(--text-dark);
  }
  .competency--intrapersonal { left: 124px; top: 492px; }
  .competency--science { left: 124px; top: 652px; }
  .competency--thinking { left: 860px; top: 492px; }
  .competency--relationships { left: 860px; top: 652px; }

  .figure-panel {
    position: absolute; left: 496px; top: 260px; width: 232px; height: 548px;
    border-radius: 110px 110px 20px 20px;
    background: linear-gradient(90deg, #8a4a2e 0%, #b86a48 45%, #c8683f 55%, #a5462c 100%);
  }
</style>
</head>
<body>
<main class="infographic">
  <svg class="graphics" width="1200" height="848" viewBox="0 0 1200 848" aria-hidden="true">
    <circle cx="608" cy="484" r="192" fill="var(--halo-grey)"/>
    <ellipse cx="600" cy="810" rx="130" ry="8" fill="var(--halo-grey)"/>

    <g fill="none" stroke="var(--ink-navy)" stroke-width="1.6">
      <polyline points="97,497 97,398 356,398"/>
      <polyline points="310,666 388,666 388,612 414,612"/>
      <polyline points="786,386 803,386 803,497 829,497"/>
      <polyline points="747,573 800,573 800,666 840,666"/>
    </g>
    <g fill="var(--text-dark)">
      <circle cx="97" cy="497" r="5"/><circle cx="356" cy="398" r="5"/>
      <circle cx="310" cy="666" r="5"/><circle cx="414" cy="612" r="5"/>
      <circle cx="786" cy="386" r="5"/><circle cx="829" cy="497" r="5"/>
      <circle cx="747" cy="573" r="5"/><circle cx="840" cy="666" r="5"/>
    </g>

    <g class="icon-pencil" fill="none" stroke="var(--ink-navy)" stroke-width="4" stroke-linejoin="round">
      <path d="M118 432 l12 -12 l38 38 l-4 16 l-16 -4 z"/>
      <path d="M124 426 l38 38"/>
      <path d="M152 470 l12 -12"/>
    </g>

    <g class="icon-atom" fill="none" stroke="var(--ink-navy)" stroke-width="4">
      <ellipse cx="76" cy="663" rx="34" ry="13"/>
      <ellipse cx="76" cy="663" rx="34" ry="13" transform="rotate(60 76 663)"/>
      <ellipse cx="76" cy="663" rx="34" ry="13" transform="rotate(-60 76 663)"/>
      <circle cx="76" cy="663" r="5"/>
    </g>

    <g class="icon-bulb" fill="none" stroke="var(--ink-navy)" stroke-width="4" stroke-linecap="round">
      <path d="M1120 504 v-10 c-8 -6 -20 -16 -20 -32 a24 24 0 0 1 48 0 c0 16 -12 26 -20 32 v10 z"/>
      <path d="M1120 510 h20 M1122 517 h16"/>
      <path d="M1124 492 v-16 l-5 -6 M1132 492 v-16 l5 -6"/>
      <path d="M1094 462 h-8 M1088 450 l-7 -3 M1088 474 l-7 3 M1162 462 h8 M1168 450 l7 -3 M1168 474 l7 3"/>
    </g>

    <g class="icon-gear" fill="none" stroke="var(--ink-navy)" stroke-width="4">
      <circle cx="1096" cy="661" r="36"/>
      <circle cx="1096" cy="661" r="26"/>
      <polygon points="1096,643 1101,650 1110,648 1108,657 1115,661 1108,665 1110,674 1101,672 1096,679 1091,672 1082,674 1084,665 1077,661 1084,657 1082,648 1091,650"/>
      <circle cx="1096" cy="661" r="7"/>
      <circle cx="1062" cy="645" r="5" fill="var(--paper)"/>
    </g>
  </svg>

  <div class="figure-panel" role="img" aria-label="Illustration of a student with a backpack, split down the middle to reveal the human muscular anatomy"></div>

  <svg class="graphics" width="1200" height="848" viewBox="0 0 1200 848" aria-hidden="true">
    <rect x="597" y="221" width="6" height="607" fill="var(--ink-navy)"/>
  </svg>

  <header class="college-name">Westbrook State University at Larkfield</header>

  <section class="statement statement--mission">
    <h2 class="statement__title">Our<br>Mission</h2>
    <p class="statement__body">To empower undergraduate students to pursue excellence through scientific discovery, clinical practice, and health promotion</p>
  </section>

  <section class="statement statement--values">
    <h2 class="statement__title">Our<br>Values</h2>
    <p class="statement__body">Student Success, Science, and Service<br>Our Graduates Will Be Competent In...</p>
    <div class="statement__arrow"></div>
  </section>

  <section class="statement statement--vision">
    <h2 class="statement__title">Our<br>Vision</h2>
    <p class="statement__body">WSUL Kinesiology graduates are leaders who excel in careers that enhance the quality of life of individuals and communities</p>
  </section>

  <section class="competency competency--intrapersonal">
    <h3 class="competency__title">Intrapersonal Growth</h3>
    <ul class="competency__list">
      <li>Cultural Humility/Sensitivity</li>
      <li>Integrity</li>
      <li>Self-Directed</li>
      <li>Dependability</li>
      <li>Mission Oriented</li>
    </ul>
  </section>

  <section class="competency competency--science">
    <h3 class="competency__title">The Science of<br>Kinesiology</h3>
    <ul class="competency__list">
      <li>Foundational Concepts of Kinesiology</li>
      <li>Clinical Application</li>
      <li>Scientific Communication</li>
    </ul>
  </section>

  <section class="competency competency--thinking">
    <h3 class="competency__title">Thinking and Reasoning</h3>
    <ul class="competency__list">
      <li>Critical Thinking</li>
      <li>Quantitative Reasoning</li>
      <li>Scientific Inquiry</li>
      <li>Concept Integration</li>
    </ul>
  </section>

  <section class="competency competency--relationships">
    <h3 class="competency__title">Relationships and<br>Communication</h3>
    <ul class="competency__list">
      <li>Cultural Competence</li>
      <li>Professionalism</li>
      <li>Leadership and Teamwork</li>
      <li>Service</li>
      <li>Orientation/Citizenship</li>
    </ul>
  </section>
</main>
</body>
</html>
```